Web site for small printshop

I am looking for a website for small printshop in Iceland, mainly serving university students and artist.

We print posters, flyers, business cards and more.

In addition to our current website, I would like to include design tool, (fx. www.quarvelink.com, www.tandorizo.com or something similar) jobs upload, shopping chart.
Updates

Great work, I am really amazed of the quality of work i am seeing here.

Really way beyond my expectation

GOOD JOB - all of you ! 

Hi all.

The designs submitted have been great, way better than expected.
I really did not expect this level of quality.

Some have been asking me for feedback on their designs, and I will try 
to send some feedback here, without spoiling your creativity.

Likes:
- when the colors of my logo is used in menus, buttons etc.
- simple, not to crowded look.

Dislikes.
- Dark and heavy design
- Lot of text and buttons (crowded look)

Extra info.
- top line (before menus) will contain: Tel - email - language
- menu line will have 5 categories: Home - service - submission of works - FAQ - about us
- 3 large buttons:  Job submit - Job design - ask for offer

LOVE YOUR WORK - great designs so far :)

Target Market(s)

University Students, Artists. Age group 20-30

Industry/Entity Type

University

Requirements
Must have
• The website must be easy to use, clean looking.

```html
<!DOCTYPE html>
<html lang="is">
<head>
<meta charset="utf-8">
<title>Tindastofa</title>
<link rel="stylesheet" href="https://fonts.googleapis.com/css2?family=PT+Sans:wght@400;700&family=PT+Sans+Narrow:wght@400;700&display=swap">
<style>
  :root {
    --red: #e8322d;
    --dark: #2b2b2b;
    --text: #3a3a3a;
    --grey: #6a6a6a;
    --orange: #f08a12;
    --orange-light: #fbb817;
    --page: #efefef;
    --white: #ffffff;
    --footer: #363636;
  }
  * { margin: 0; padding: 0; box-sizing: border-box; }
  html, body { width: 974px; height: 1200px; overflow: hidden; }
  body {
    position: relative;
    background: var(--page);
    font-family: "PT Sans", Arial, sans-serif;
    color: var(--text);
  }
  .site-header {
    position: absolute; left: 0; top: 0; width: 974px; height: 88px;
    background: linear-gradient(#ffffff, #f4f4f4);
  }
  .brand { position: absolute; left: 124px; top: 26px; display: flex; align-items: center; gap: 10px; }
  .brand-mark { width: 26px; height: 26px; border-radius: 50%; background: var(--red); }
  .brand-name { font-size: 32px; font-weight: 400; color: var(--dark); line-height: 1; }
  .main-nav { position: absolute; top: 34px; left: 524px; display: flex; align-items: center; height: 26px; }
  .main-nav a {
    font-size: 12px; color: #444; text-decoration: none; padding: 0 12px; height: 26px; line-height: 26px;
    border-left: 1px solid #dcdcdc;
  }
  .main-nav a.is-active { background: var(--red); color: var(--white); border-radius: 2px; border: none; margin-right: 4px; padding: 0 9px; }
  .main-nav a.after-active { border-left: none; }
  .hero-band {
    position: absolute; left: 0; top: 88px; width: 974px; height: 346px;
    background: radial-gradient(ellipse at 50% 0%, var(--orange-light), var(--orange) 55%);
  }
  .slider {
    position: absolute; left: 98px; top: 127px; width: 779px; height: 355px;
    background: var(--white); box-shadow: 0 6px 10px rgba(0,0,0,0.18);
  }
  .slide-image {
    position: absolute; left: 8px; top: 8px; width: 763px; height: 340px;
    background: linear-gradient(180deg, #8c8a86 0%, #5e5a54 45%, #3a3632 100%);
  }
  .slide-caption {
    position: absolute; left: 32px; top: 206px; color: var(--white);
    font-family: "PT Sans Narrow", "PT Sans", sans-serif; font-size: 21px; line-height: 24px;
  }
  .slide-dots { position: absolute; left: 691px; top: 314px; display: flex; gap: 5px; }
  .slide-dots span { width: 14px; height: 14px; border-radius: 50%; background: #d8d8d8; border: 2px solid #fff; }
  .slide-dots span.is-current { background: #d33b14; }
  .steps { position: absolute; top: 532px; left: 0; width: 974px; }
  .step {
    position: absolute; width: 170px; height: 170px; border-radius: 50%;
    background: radial-gradient(circle at 50% 40%, #ffffff 60%, #f0f0f0);
    box-shadow: 0 0 0 1px #e2e2e2;
  }
  .step-badge {
    position: absolute; left: 8px; top: -6px; width: 56px; height: 56px; border-radius: 50%;
    background: radial-gradient(circle, #f9b41c, #ee5a1d);
    color: var(--white); font-size: 18px; text-align: center; line-height: 56px;
  }
  .step-icon { position: absolute; left: 43px; top: 52px; width: 86px; height: 68px; background: linear-gradient(#cfd8e4, #8aa0b8); border-radius: 4px; }
  .step-label { position: absolute; left: 0; width: 170px; top: 126px; text-align: center; font-size: 16px; color: #555; }
  .content {
    position: absolute; left: 122px; top: 741px; width: 734px; height: 359px; background: var(--white);
  }
  .welcome { position: absolute; left: 17px; top: 20px; font-size: 21px; font-weight: 400; color: var(--dark); }
  .welcome em { font-style: normal; color: var(--red); }
  .services { position: absolute; left: 17px; top: 60px; width: 468px; }
  .service { margin-bottom: 12px; }
  .service h3 { font-size: 10px; font-weight: 400; color: var(--red); line-height: 14px; }
  .service p { font-size: 9.6px; line-height: 14.6px; text-align: justify; color: var(--text); }
  .learn-more {
    position: absolute; left: 417px; top: 293px; width: 68px; height: 21px; background: var(--red);
    color: var(--white); border-radius: 3px; text-align: center; line-height: 21px;
    font-family: "PT Sans Narrow", "PT Sans", sans-serif; font-size: 12px; text-decoration: none;
  }
  .location { position: absolute; left: 529px; top: 30px; }
  .location h2 { font-size: 15px; font-weight: 400; color: var(--dark); margin-bottom: 5px; }
  .location-map { width: 158px; height: 125px; background: linear-gradient(135deg, #dcdcdc, #c8ccd2); }
  .address { margin: 10px 0 0 12px; font-style: normal; font-size: 11px; line-height: 17px; color: #555; }
  .site-footer {
    position: absolute; left: 0; top: 1100px; width: 974px; height: 100px; background: var(--footer);
    border-top: 6px solid #2a2a2a;
  }
  .social { position: absolute; left: 128px; top: 31px; display: flex; gap: 3px; }
  .social a { width: 25px; height: 25px; border-radius: 50%; background: #e6e6e6; display: block; }
  .copyright { position: absolute; right: 115px; top: 24px; font-size: 9px; color: #e0e0e0; }
</style>
</head>
<body>
  <header class="site-header">
    <div class="brand">
      <span class="brand-mark"></span>
      <span class="brand-name">Tindastofa</span>
    </div>
    <nav class="main-nav">
      <a class="is-active" href="#">Home</a>
      <a class="after-active" href="#">About Us</a>
      <a href="#">Services</a>
      <a href="#">Demo</a>
      <a href="#">Blog</a>
      <a href="#">Contact</a>
    </nav>
  </header>

  <div class="hero-band"></div>
  <section class="slider">
    <div class="slide-image" role="img" aria-label="Photo of the print shop storefront with sample business cards"></div>
    <div class="slide-caption">Printing Posters<br>Flyers<br>Business Cards</div>
    <div class="slide-dots"><span class="is-current"></span><span></span><span></span></div>
  </section>

  <section class="steps">
    <div class="step" style="left:154px">
      <div class="step-icon" role="img" aria-label="Design software window illustration"></div>
      <div class="step-badge">1</div>
      <div class="step-label">Creating</div>
    </div>
    <div class="step" style="left:399px">
      <div class="step-icon" role="img" aria-label="Drive with upload arrow illustration"></div>
      <div class="step-badge">2</div>
      <div class="step-label">Uploading</div>
    </div>
    <div class="step" style="left:635px">
      <div class="step-icon" role="img" aria-label="Printed photos illustration"></div>
      <div class="step-badge">3</div>
      <div class="step-label">Getting</div>
    </div>
  </section>

  <main class="content">
    <h1 class="welcome">Welcome to <em>Tindastofa</em></h1>
    <div class="services">
      <div class="service">
        <h3>LJÓSRITUN</h3>
        <p>Við tökum að okkar að ljósrita í lit eða svart hvítu, við fjölritum námshefti, námsgögn, greinasöfn, MA ritgerðir, BA ritgerðir, handrit, spurningalista og fleira og bindum inn á þann hátt sem hentar. Við gormum, kjöllimum og heftum, brjótum og skerum; allt eftir þínu höfði. Við skönnum inn í tölvu á hvaða formi sem hentar þér.</p>
      </div>
      <div class="service">
        <h3>PRENTUN</h3>
        <p>Við sjáum um alla almenna prentun, til dæmis prentum við: bæklinga, dreifibréf, tímarit, nafnspjöld, ársskýrslur, boðskort, ráðstefnugögn, markpóst, plaköt og skilum því eins og hentar þér best. Við getum prentað á fjölmargar tegundir pappírs, þykkan, þunnan, gljáandi eða mattan.</p>
      </div>
      <div class="service">
        <h3>BÓKAÚTGÁFA.</h3>
        <p>Við gefum út bækur, ekkert upplag er of lítið eða stórt. Við höfum prentað námsbækur, kennslubækur, barnabækur, spennubækur, eða allar tegundir bóka. Við skilum bókum sem kilju, harðspjaldabók, í möppu, leðurbundið eða hvað sem hentar. Við getum skannað inn gamlar bækur og endurútgefið.</p>
      </div>
    </div>
    <a class="learn-more" href="#">learn more</a>

    <aside class="location">
      <h2>Hvar erum við:</h2>
      <div class="location-map" role="img" aria-label="Street map showing the shop location"></div>
      <address class="address">
        Tindastofa<br>
        Hrafnagata 9<br>
        107 - Reykjavík<br>
        Sími: 555 0142<br>
        verk@tindastofa.is<br>
        Opnunartími<br>
        Mán - fös: 9 - 17<br>
        lokað um helgar
      </address>
    </aside>
  </main>

  <footer class="site-footer">
    <nav class="social" aria-label="Social links">
      <a href="#" aria-label="Social link 1"></a>
      <a href="#" aria-label="Social link 2"></a>
      <a href="#" aria-label="Social link 3"></a>
      <a href="#" aria-label="Social link 4"></a>
      <a href="#" aria-label="Social link 5"></a>
      <a href="#" aria-label="Social link 6"></a>
    </nav>
    <p class="copyright">© 2013 tindastofa, All rights reserved</p>
  </footer>
</body>
</html>
```